Landing Page and Logo for Auto-Blogging Platform

I created a platform that allows users to start a blog for their business, hobby, charity, etc. I need a landing page where users can learn about the platform, benefits of consistent blogging, SEO value, plans/pricing, etc. The landing page needs to have multiple call to action buttons encouraging the visitor to register/sign up for a free trial.

In addition to the landing page, I need a page for users to establish the settings for their blog. This page should be a fairly simple form, intended for the user to enter a few details to set up their blog:
1. Name of Blog
2. Up to 10 topics and/or keywords the blog should focus on
3. Theme: Color-scheme and logo upload for blog.

I have attached the specifications of the platform's functionality so you can better understand how it works, plans/pricing, etc.

I also need a logo for the business. The name of the platform is PostNook.

Target Market(s)

Website owners, bloggers, business owners

Industry/Entity Type

Technology, Internet, web design

Coding

Coded - Design and coding required

Number of Pages Required

2 page

Colors
0054AA
0677BA
7BADD7
CADEEF
E8F1F8
0094D4
00A9DD
6FCCEA
C7EBF8
E9F6FB

Requirements
Must have
• Eye-catching design but fairly light on content (keep it simple and brief.)
Nice to have
• Eye-catching yet simple design, clean and easy to understand what we are offering.
Should not have
• Too much “wordy” and confusing content.

```html
<!DOCTYPE html>
<html lang="en">
<head>
<meta charset="utf-8">
<title>PostNook – Auto-Blogging Platform</title>
<link rel="stylesheet" href="https://fonts.googleapis.com/css2?family=Poppins:wght@300;400;500;600;700;800&display=swap">
<style>
  :root {
    --panel: #1b4fa3;
    --deep: #1a4a9c;
    --cyan-light: #72cfe2;
    --cyan: #45bfe0;
    --sky: #2aa0d8;
    --yellow: #f8d43f;
    --white: #ffffff;
    --ink: #1d2433;
    --page: #ffffff;
  }
  * { box-sizing: border-box; margin: 0; padding: 0; }
  html, body { width: 1200px; height: 2933px; overflow: hidden; background: var(--page); }
  body { position: relative; font-family: "Poppins", sans-serif; color: var(--white); }

  .panel { position: absolute; left: 30px; width: 1141px; background: var(--panel); }
  .panel--home { top: 38px; height: 1367px; }
  .panel--setup { top: 1432px; height: 713px; }
  .panel--pricing { top: 2172px; height: 714px; }

  .nav { position: absolute; left: 0; top: 0; width: 100%; height: 110px; }
  .brand { position: absolute; left: 43px; top: 36px; display: flex; align-items: center; gap: 9px;
           font-size: 29px; font-weight: 600; color: var(--white); letter-spacing: -0.3px; }
  .brand__dot { width: 30px; height: 30px; border-radius: 50%; background: var(--white); }
  .nav__link { position: absolute; top: 43px; font-size: 18px; font-weight: 400; color: var(--white); }
  .nav__link--active { font-weight: 700; }
  .nav__link--home { left: 403px; }
  .nav__link--services { left: 512px; }
  .nav__link--pricing { left: 626px; }
  .nav__link--setup { left: 736px; }
  .nav__link--about { left: 831px; top: 42px; }
  .nav__signup { position: absolute; left: 962px; top: 37px; width: 133px; height: 38px; border-radius: 19px;
                 background: var(--yellow); color: var(--ink); font-size: 18px; font-weight: 500;
                 display: flex; align-items: center; justify-content: center; }

  .card { position: absolute; border-radius: 22px; overflow: hidden; }
  .card--hero { left: 44px; top: 125px; width: 1051px; height: 528px;
                background: linear-gradient(115deg, #5ccbe0 0%, #2aa6dc 38%, #1f63b5 68%, var(--panel) 100%); }
  .card--steps { left: 44px; top: 687px; width: 1051px; height: 680px; border-radius: 22px 22px 0 0;
                 background: linear-gradient(180deg, #72cfe2 0%, #48c2e2 22%, #2a9ad6 50%, #1f5fb2 78%, var(--panel) 92%); }
  .card--form { left: 44px; top: 124px; width: 1051px; height: 529px;
                background: linear-gradient(110deg, #74cfe0 0%, #3dbae0 35%, #1f6fbb 65%, var(--panel) 100%); }

  .tag { position: absolute; left: 46px; height: 33px; width: 174px; border-radius: 17px; background: var(--white);
         color: var(--ink); font-size: 16px; display: flex; align-items: center; justify-content: center; }
  .title { position: absolute; left: 46px; font-size: 32px; font-weight: 800; line-height: 34px; letter-spacing: 0.2px; }
  .lede { position: absolute; left: 46px; font-size: 19px; line-height: 22.5px; font-weight: 400; }

  .pill-cta { position: absolute; height: 52px; width: 248px; border-radius: 26px; background: var(--white);
              color: var(--ink); font-size: 19px; display: flex; align-items: center; padding-left: 44px; }
  .pill-cta__arrow { position: absolute; right: 6px; top: 6px; width: 40px; height: 40px; border-radius: 50%;
                     background: var(--yellow); display: flex; align-items: center; justify-content: center; }

  .hero-photo { position: absolute; left: 535px; top: 44px; width: 474px; height: 440px;
                background: linear-gradient(140deg, #e9e6e2 0%, #bdb3aa 40%, #6d5547 65%, #cfd3d8 100%);
                clip-path: polygon(22% 0, 84% 0, 100% 22%, 100% 86%, 88% 100%, 42% 100%, 0 47%, 0 40%); }

  .steps-art { position: absolute; top: 263px; height: 207px; border-radius: 6px;
               background: linear-gradient(160deg, #f6d548 0%, #e8c23a 45%, #2a3f8f 100%); }
  .steps-art--1 { left: 46px; width: 218px; }
  .steps-art--2 { left: 302px; width: 227px; }
  .steps-art--3 { left: 569px; width: 226px; }
  .steps-art--4 { left: 832px; width: 200px; }
  .step-caption { position: absolute; top: 490px; font-size: 16.5px; line-height: 20px; text-align: center; white-space: nowrap; }
  .step-caption--1 { left: 36px; width: 238px; }
  .step-caption--2 { left: 292px; width: 247px; }
  .step-caption--3 { left: 559px; width: 246px; }
  .step-caption--4 { left: 812px; width: 240px; }
  .steps-cta { position: absolute; left: 401px; top: 582px; width: 249px; height: 52px; border-radius: 26px;
               background: var(--yellow); color: var(--ink); font-size: 19px;
               display: flex; align-items: center; justify-content: center; }

  .field-label { position: absolute; left: 526px; font-size: 19px; font-weight: 600; }
  .field { position: absolute; left: 526px; width: 458px; border-radius: 6px; background: var(--white); }
  .field--upload { display: flex; align-items: center; justify-content: center; }

  .plan { position: absolute; top: 136px; width: 338px; height: 532px; border-radius: 20px;
          background: linear-gradient(165deg, #4cc3e2 0%, #2ba2d9 35%, #2278c3 70%, #1e5fb1 100%); }
  .plan--base { left: 44px; }
  .plan--premium { left: 400px; border: 1.5px solid rgba(160, 220, 245, 0.7); }
  .plan--ultimate { left: 758px; }
  .plan__badge { position: absolute; right: 8px; top: 9px; width: 114px; height: 33px; border-radius: 17px;
                 background: var(--yellow); color: var(--ink); font-size: 17px;
                 display: flex; align-items: center; justify-content: center; }
  .plan__name { position: absolute; left: 46px; top: 64px; font-size: 29px; font-weight: 800; }
  .plan__price { position: absolute; left: 45px; top: 112px; font-size: 48px; font-weight: 800; letter-spacing: -0.5px; }
  .plan__cycle { position: absolute; left: 46px; top: 194px; font-size: 16.5px; }
  .plan__cycle b { font-weight: 700; }
  .plan__feature { position: absolute; left: 46px; display: flex; align-items: center; gap: 12px;
                   font-size: 19px; line-height: 22px; font-weight: 300; }
  .plan__feature svg { flex: none; }
  .plan .pill-cta { left: 46px; top: 436px; padding-left: 26px; font-size: 18px; }
</style>
</head>
<body>

<!-- Landing page -->
<section class="panel panel--home">
  <nav class="nav">
    <div class="brand"><span class="brand__dot"></span>PostNook</div>
    <span class="nav__link nav__link--home nav__link--active">Home</span>
    <span class="nav__link nav__link--services">Services</span>
    <span class="nav__link nav__link--pricing">Pricing</span>
    <span class="nav__link nav__link--setup">Set Up</span>
    <span class="nav__link nav__link--about">About</span>
    <span class="nav__signup">Sign up</span>
  </nav>

  <div class="card card--hero">
    <span class="tag" style="top:68px">#StartYourBlog</span>
    <h1 class="title" style="top:148px">Automate Your Blog<br>Posting with AI</h1>
    <p class="lede" style="top:232px;width:375px">Enhance your SEO by consistently publishing fresh, keyword-targeted content. Let AI keep your blog updated and optimized, so you can focus on your business.</p>
    <span class="pill-cta" style="left:46px;top:378px">Start free trial
      <span class="pill-cta__arrow"><svg width="18" height="14" viewBox="0 0 18 14"><path d="M1 7h15M10 1l6 6-6 6" fill="none" stroke="#1d2433" stroke-width="1.8" stroke-linecap="round" stroke-linejoin="round"/></svg></span>
    </span>
    <div class="hero-photo" role="img" aria-label="Photo of hands typing on a laptop beside a cup of coffee on a speckled desk"></div>
  </div>

  <div class="card card--steps">
    <h2 class="title" style="top:58px">How to Set Up Your Auto-Blog<br>in 4 Easy Steps</h2>
    <p class="lede" style="top:140px;width:490px">Follow these quick steps to launch your blog. Customize it, set your posting schedule, add your blog name, and select your topics—or let AI handle the rest. It’s that easy!</p>

    <div class="steps-art steps-art--1" role="img" aria-label="Step 1 illustration: woman in a yellow sweater choosing a posting frequency on a tablet"></div>
    <div class="steps-art steps-art--2" role="img" aria-label="Step 2 illustration: woman typing a blog name on a laptop"></div>
    <div class="steps-art steps-art--3" role="img" aria-label="Step 3 illustration: woman choosing blog topics or letting AI choose"></div>
    <div class="steps-art steps-art--4" role="img" aria-label="Step 4 illustration: woman relaxing with a drink while AI blogs"></div>

    <p class="step-caption step-caption--1">Select how often you want<br>Automated Blog Posts<br>daily, weekly, or monthly.</p>
    <p class="step-caption step-caption--2">Give your blog a name<br>that reflects its purpose or<br>personality.</p>
    <p class="step-caption step-caption--3">Select the topics for<br>your blog, or let AI<br>choose them for you</p>
    <p class="step-caption step-caption--4">Relax and let AI handle<br>all your blogging for you!</p>

    <span class="steps-cta">Start free trial</span>
  </div>
</section>

<!-- Blog setup page -->
<section class="panel panel--setup">
  <nav class="nav">
    <div class="brand"><span class="brand__dot"></span>PostNook</div>
    <span class="nav__link nav__link--home">Home</span>
    <span class="nav__link nav__link--services">Services</span>
    <span class="nav__link nav__link--pricing">Pricing</span>
    <span class="nav__link nav__link--setup nav__link--active">Set Up</span>
    <span class="nav__link nav__link--about">About</span>
    <span class="nav__signup">Sign up</span>
  </nav>

  <div class="card card--form">
    <span class="tag" style="top:69px">#StartYourBlog</span>
    <h1 class="title" style="top:150px">Set Up Your Blog:<br>Customize and Personalize</h1>
    <p class="lede" style="top:234px;width:420px">Get your blog ready in just a few steps. Fill out the form below to name your blog, choose focus topics, and customize your theme. With these simple settings, you’ll be on your way to creating a blog that truly represents you and your brand.</p>

    <span class="field-label" style="top:46px">Blog Name</span>
    <div class="field" style="top:80px;height:43px"></div>
    <span class="field-label" style="top:143px">Focus Topics &amp; Keywords</span>
    <div class="field" style="top:177px;height:92px"></div>
    <span class="field-label" style="top:292px">Theme Customization</span>
    <div class="field" style="top:326px;height:43px"></div>
    <span class="field-label" style="top:380px">Upload Your Logo</span>
    <div class="field field--upload" style="top:414px;height:59px">
      <svg width="40" height="30" viewBox="0 0 40 30"><path d="M12 24H9a7 7 0 0 1-1-13.9A10 10 0 0 1 27 8a8 8 0 0 1 4 16h-3" fill="none" stroke="#1f5fb2" stroke-width="1.6" stroke-linecap="round" stroke-linejoin="round"/><path d="M20 28V15M15 19l5-5 5 5" fill="none" stroke="#1f5fb2" stroke-width="1.6" stroke-linecap="round" stroke-linejoin="round"/></svg>
    </div>
  </div>
</section>

<!-- Pricing page -->
<section class="panel panel--pricing">
  <nav class="nav">
    <div class="brand"><span class="brand__dot"></span>PostNook</div>
    <span class="nav__link nav__link--home">Home</span>
    <span class="nav__link nav__link--services">Services</span>
    <span class="nav__link nav__link--pricing nav__link--active">Pricing</span>
    <span class="nav__link nav__link--setup">Set Up</span>
    <span class="nav__link nav__link--about">About</span>
    <span class="nav__signup">Sign up</span>
  </nav>

  <article class="plan plan--base">
    <h2 class="plan__name">Base Plan</h2>
    <p class="plan__price">$9.99/mo</p>
    <p class="plan__cycle">For <b>every month</b> you will get</p>
    <p class="plan__feature" style="top:282px"><svg width="18" height="14" viewBox="0 0 18 14"><path d="M1 7l5 5L17 1" fill="none" stroke="#fff" stroke-width="1.5"/></svg>1 blog post</p>
    <p class="plan__feature" style="top:319px"><svg width="18" height="14" viewBox="0 0 18 14"><path d="M1 7l5 5L17 1" fill="none" stroke="#fff" stroke-width="1.5"/></svg>Up to 2,000 words</p>
    <span class="pill-cta">SUBSCRIBE NOW
      <span class="pill-cta__arrow"><svg width="18" height="14" viewBox="0 0 18 14"><path d="M1 7h15M10 1l6 6-6 6" fill="none" stroke="#1d2433" stroke-width="1.8" stroke-linecap="round" stroke-linejoin="round"/></svg></span>
    </span>
  </article>

  <article class="plan plan--premium">
    <span class="plan__badge">#bestdeal</span>
    <h2 class="plan__name">Premium Plan</h2>
    <p class="plan__price">$14.99/mo</p>
    <p class="plan__cycle">For <b>every week</b> you will get</p>
    <p class="plan__feature" style="top:286px"><svg width="18" height="14" viewBox="0 0 18 14"><path d="M1 7l5 5L17 1" fill="none" stroke="#fff" stroke-width="1.5"/></svg>1 blog post</p>
    <p class="plan__feature" style="top:323px"><svg width="18" height="14" viewBox="0 0 18 14"><path d="M1 7l5 5L17 1" fill="none" stroke="#fff" stroke-width="1.5"/></svg>Up to 2,000 words</p>
    <span class="pill-cta">SUBSCRIBE NOW
      <span class="pill-cta__arrow"><svg width="18" height="14" viewBox="0 0 18 14"><path d="M1 7h15M10 1l6 6-6 6" fill="none" stroke="#1d2433" stroke-width="1.8" stroke-linecap="round" stroke-linejoin="round"/></svg></span>
    </span>
  </article>

  <article class="plan plan--ultimate">
    <h2 class="plan__name">Ultimate Plan</h2>
    <p class="plan__price">$24.99/mo</p>
    <p class="plan__cycle">For <b>every day</b> you will get</p>
    <p class="plan__feature" style="top:246px"><svg width="18" height="14" viewBox="0 0 18 14"><path d="M1 7l5 5L17 1" fill="none" stroke="#fff" stroke-width="1.5"/></svg>1 blog post</p>
    <p class="plan__feature" style="top:298px"><svg width="18" height="14" viewBox="0 0 18 14"><path d="M1 7l5 5L17 1" fill="none" stroke="#fff" stroke-width="1.5"/></svg>Up to 3,000 words</p>
    <p class="plan__feature" style="top:344px"><svg width="18" height="14" viewBox="0 0 18 14"><path d="M1 7l5 5L17 1" fill="none" stroke="#fff" stroke-width="1.5"/></svg>Unlimited manual<br>posting</p>
    <span class="pill-cta">SUBSCRIBE NOW
      <span class="pill-cta__arrow"><svg width="18" height="14" viewBox="0 0 18 14"><path d="M1 7h15M10 1l6 6-6 6" fill="none" stroke="#1d2433" stroke-width="1.8" stroke-linecap="round" stroke-linejoin="round"/></svg></span>
    </span>
  </article>
</section>

</body>
</html>
```